The Guiding Spark LLC
because everyone deserves a fan
The Guiding Spark LLC -
Creative Brief
Bright & Fun-filled
Rosalind K Delgado
Personal Mentor
2871 S Whitcomb Ave Garden Unit Chicago IL 60619
rdelgado@theguidingspark.example
www.theguidingspark.example
Our Time Together Date: Time: Ask about our Friend Bonus program

```html
<!DOCTYPE html>
<html lang="en">
<head>
<meta charset="utf-8">
<title>The Guiding Spark LLC — Stationery Suite</title>
<link rel="stylesheet" href="https://fonts.googleapis.com/css2?family=Open+Sans:wght@400;600;700;800&display=swap">
<style>
:root{
  --backdrop:#e9e7e3;
  --paper:#ffffff;
  --ink:#3a3a3a;
  --ink-soft:#6b6b6b;
  --blue-deep:#0a3a86;
  --blue:#1763bd;
  --blue-light:#4ea4e2;
  --green:#5cb646;
  --green-deep:#2f8d33;
  --glow:rgba(255,205,85,.55);
  --rule:#b9b9b9;
}
*{box-sizing:border-box;margin:0;padding:0}
html,body{width:1200px;height:935px;overflow:hidden}
body{background:var(--backdrop);font-family:"Open Sans",Arial,sans-serif;color:var(--ink)}
.suite{position:relative;width:1200px;height:935px}

.sheet{position:absolute;background:var(--paper);overflow:hidden;box-shadow:0 2px 8px rgba(0,0,0,.18)}
.sheet::after{content:"";position:absolute;inset:0;pointer-events:none;
  background:radial-gradient(ellipse 38% 26% at 82% 96%,var(--glow),transparent 100%)}
.band{position:absolute;left:0;top:0;width:100%;height:100%}

.mark{position:absolute;display:flex;align-items:center;z-index:2}
.mark-dot{border-radius:50%;background:var(--paper);border:3px solid var(--blue-light);flex:none}
.mark-name{color:var(--blue);font-weight:600;white-space:nowrap;line-height:1}

/* fax */
.fax{left:38px;top:157px;width:570px;height:740px}
.fax .mark{left:14px;top:18px}
.fax .mark-dot{width:38px;height:38px}
.fax .mark-name{font-size:12px;margin-left:8px}
.fax-title{position:absolute;left:76px;top:190px;font-size:44px;font-weight:800;color:#111;letter-spacing:1px;z-index:2}
.fax-fields{position:absolute;left:76px;top:278px;width:440px;list-style:none;z-index:2}
.fax-fields li{display:flex;align-items:flex-end;height:40px;font-size:11px;font-weight:700}
.fax-fields li span{width:48px}
.fax-fields li i{flex:1;border-bottom:1px dotted var(--rule);height:1px}
.fax-checks{position:absolute;left:76px;top:480px;display:flex;gap:36px;font-size:10px;z-index:2}
.fax-checks label{display:flex;align-items:center;gap:6px}
.fax-checks b{width:10px;height:10px;border:1px solid var(--ink-soft);display:inline-block}
.fax-footer{position:absolute;left:76px;top:668px;font-size:8.5px;line-height:1.45;color:var(--ink);z-index:2}

/* letterhead */
.letterhead{left:202px;top:56px;width:570px;height:776px}
.letterhead .mark{left:20px;top:24px}
.letterhead .mark-dot{width:58px;height:58px}
.letterhead .mark-name{font-size:24px;margin-left:14px}
.letterhead-footer{position:absolute;left:76px;top:676px;font-size:8.5px;line-height:1.5;z-index:2}

/* envelope */
.envelope{left:524px;top:215px;width:602px;height:455px;background:transparent;box-shadow:none;overflow:visible}
.envelope::after{display:none}
.envelope-flap{position:absolute;left:0;top:0;width:602px;height:112px}
.envelope-flap .mark{left:50%;top:30px;transform:translateX(-50%) rotate(180deg)}
.envelope-flap .mark-dot{width:34px;height:34px}
.envelope-flap .mark-name{font-size:18px;margin-left:10px}
.envelope-front{position:absolute;left:0;top:110px;width:602px;height:345px;background:var(--paper);overflow:hidden;box-shadow:0 2px 8px rgba(0,0,0,.18)}
.envelope-front::after{content:"";position:absolute;inset:0;pointer-events:none;
  background:radial-gradient(ellipse 36% 34% at 78% 100%,var(--glow),transparent 100%)}
.envelope-front .mark{left:18px;top:16px}
.envelope-front .mark-dot{width:54px;height:54px}
.envelope-front .mark-name{font-size:23px;margin-left:12px}
.return-address{position:absolute;left:58px;top:104px;font-size:8.5px;line-height:1.5;z-index:2}

/* business card */
.business-card{left:855px;top:50px;width:305px;height:140px;border-radius:8px}
.business-card .mark{left:10px;top:12px}
.business-card .mark-dot{width:36px;height:36px}
.business-card .mark-name{font-size:15px;margin-left:9px}
.card-contact{position:absolute;left:92px;top:56px;font-size:6.5px;line-height:1.5;z-index:2}
.card-contact .person{font-size:9px;font-weight:700}
.card-contact .role{font-size:7px;margin-bottom:3px;color:var(--ink-soft)}

/* appointment cards */
.appointment{border-radius:8px;color:var(--paper)}
.appointment::after{display:none}
.appointment-blue{left:906px;top:602px;width:220px;height:132px;
  background:linear-gradient(135deg,var(--blue-light),var(--blue) 45%,var(--blue-deep))}
.appointment-green{left:817px;top:751px;width:304px;height:147px;
  background:linear-gradient(135deg,#9bd66a,var(--green) 45%,var(--green-deep))}
.appointment .mark-name{color:var(--paper)}
.appointment-blue .mark{left:50%;top:8px;transform:translateX(-50%);flex-direction:column}
.appointment-blue .mark-dot{width:26px;height:26px;border-width:2px}
.appointment-blue .mark-name{font-size:11px;margin-top:4px}
.appointment-green .mark{left:12px;top:12px}
.appointment-green .mark-dot{width:34px;height:34px;border-width:2px;border-color:#d9f2c8}
.appointment-green .mark-name{font-size:15px;margin-left:9px}
.appointment-panel{position:absolute;left:12px;right:12px;bottom:12px;background:var(--paper);border-radius:5px;color:var(--ink);padding:6px 9px;font-size:6.5px;line-height:1.55}
.appointment-blue .appointment-panel{top:58px}
.appointment-green .appointment-panel{top:58px;font-size:7.5px;padding:8px 12px}
.appointment-panel strong{font-size:1.15em;display:block}
.appointment-panel .slot{display:flex;gap:8px}
.appointment-panel .slot span{flex:1;border-bottom:1px solid var(--rule)}
</style>
</head>
<body>
<main class="suite">

<svg width="0" height="0" style="position:absolute" aria-hidden="true">
  <defs>
    <linearGradient id="bandFill" x1="0" y1="0" x2="1" y2="0">
      <stop offset="0" stop-color="#0a3a86"/>
      <stop offset=".7" stop-color="#1763bd"/>
      <stop offset="1" stop-color="#4ea4e2"/>
    </linearGradient>
    <linearGradient id="flapFill" x1="0" y1="0" x2="0" y2="1">
      <stop offset="0" stop-color="#ffffff"/>
      <stop offset="1" stop-color="#e4e4e4"/>
    </linearGradient>
  </defs>
</svg>

<!-- fax cover -->
<section class="sheet fax">
  <svg class="band" viewBox="0 0 100 100" preserveAspectRatio="none" aria-hidden="true">
    <path d="M0 0H17C12 20 9 50 8 100H0Z" fill="url(#bandFill)"/>
    <path d="M19 0C14 20 11 50 10 100" fill="none" stroke="#5cb646" stroke-width="3" vector-effect="non-scaling-stroke"/>
  </svg>
  <div class="mark"><span class="mark-dot"></span><span class="mark-name">The Guiding Spark</span></div>
  <h1 class="fax-title">FAX</h1>
  <ul class="fax-fields">
    <li><span>To :</span><i></i></li>
    <li><span>Cc :</span><i></i></li>
    <li><span>Phone :</span><i></i></li>
    <li><span>Re :</span><i></i></li>
  </ul>
  <div class="fax-checks">
    <label><b></b>Urgent</label>
    <label><b></b>For Review</label>
    <label><b></b>Please Reply</label>
  </div>
  <address class="fax-footer">
    2871 S Whitcomb Ave, Garden Unit, Chicago IL 60619<br>
    Phone: 312.555.0147 &nbsp;|&nbsp; Email: rdelgado@theguidingspark.example<br>
    Web: www.theguidingspark.example
  </address>
</section>

<!-- letterhead -->
<section class="sheet letterhead">
  <svg class="band" viewBox="0 0 100 100" preserveAspectRatio="none" aria-hidden="true">
    <path d="M0 0H17C12 20 9 50 8 100H0Z" fill="url(#bandFill)"/>
    <path d="M19 0C14 20 11 50 10 100" fill="none" stroke="#5cb646" stroke-width="3" vector-effect="non-scaling-stroke"/>
  </svg>
  <div class="mark"><span class="mark-dot"></span><span class="mark-name">The Guiding Spark</span></div>
  <address class="letterhead-footer">
    2871 S Whitcomb Ave, Garden Unit, Chicago IL 60619<br>
    Phone: 312.555.0147 &nbsp;|&nbsp; Email: rdelgado@theguidingspark.example<br>
    Web: www.theguidingspark.example
  </address>
</section>

<!-- envelope -->
<section class="sheet envelope">
  <div class="envelope-flap">
    <svg width="602" height="112" viewBox="0 0 602 112" aria-hidden="true" style="position:absolute;left:0;top:0">
      <path d="M0 112L46 6Q50 0 58 0H544Q552 0 556 6L602 112Z" fill="url(#flapFill)" stroke="#d2d2d2"/>
    </svg>
    <div class="mark"><span class="mark-dot"></span><span class="mark-name">The Guiding Spark</span></div>
  </div>
  <div class="envelope-front">
    <svg class="band" viewBox="0 0 100 100" preserveAspectRatio="none" aria-hidden="true">
      <path d="M0 0H14C10 25 8 60 7 100H0Z" fill="url(#bandFill)"/>
      <path d="M15.5 0C11.5 25 9.5 60 8.5 100" fill="none" stroke="#5cb646" stroke-width="3" vector-effect="non-scaling-stroke"/>
    </svg>
    <div class="mark"><span class="mark-dot"></span><span class="mark-name">The Guiding Spark</span></div>
    <address class="return-address">
      2871 S Whitcomb Ave<br>Garden Unit, Chicago IL 60619
    </address>
  </div>
</section>

<!-- business card -->
<section class="sheet business-card">
  <svg class="band" viewBox="0 0 100 100" preserveAspectRatio="none" aria-hidden="true">
    <path d="M0 0H17C13 30 11 60 10 100H0Z" fill="url(#bandFill)"/>
    <path d="M19 0C15 30 13 60 12 100" fill="none" stroke="#5cb646" stroke-width="2" vector-effect="non-scaling-stroke"/>
  </svg>
  <div class="mark"><span class="mark-dot"></span><span class="mark-name">The Guiding Spark</span></div>
  <address class="card-contact">
    <div class="person">Rosalind K Delgado</div>
    <div class="role">Personal Mentor</div>
    2871 S Whitcomb Ave, Garden Unit, Chicago IL 60619<br>
    Phone: 312.555.0147<br>
    rdelgado@theguidingspark.example<br>
    www.theguidingspark.example
  </address>
</section>

<!-- appointment card, blue -->
<section class="sheet appointment appointment-blue">
  <div class="mark"><span class="mark-dot"></span><span class="mark-name">The Guiding Spark</span></div>
  <div class="appointment-panel">
    <strong>Our Time Together</strong>
    <div class="slot">Date: <span></span> Time: <span></span></div>
    Ask about our Friend Bonus program
  </div>
</section>

<!-- appointment card, green -->
<section class="sheet appointment appointment-green">
  <div class="mark"><span class="mark-dot"></span><span class="mark-name">The Guiding Spark</span></div>
  <div class="appointment-panel">
    <strong>Our Time Together</strong>
    <div class="slot">Date: <span></span> Time: <span></span></div>
    Ask about our Friend Bonus program
  </div>
</section>

</main>
</body>
</html>
```